Need UI design for an iOS app game with most of the layout planned

The name of the game is "QUADRIX".

The goal of the game is to find a way to manipulate four numbers so that the end result is 24. Addition, subtraction, multiplication and division may be used and each number can only be used once.

The list of items we need is:

1. launch image, app icon, UI design of all scenes (10-12 scenes) of the app.
2. App background image should support screen size of both 640x1136.
3. Files are preferred to be in (.eps) format so that resolution can be adjusted later. But other file formats are welcome as long as resolution is high enough.
4. Icons, buttons, background image etc. should have their own file so that later they can be moved around in case design is changed.

The detailed requirement is in the attached file. The actual layout can vary if it can help achieve better result. We also attached several screenshots from iOS game "Glimtor". You can use that as your reference.

```html
<!DOCTYPE html>
<html lang="en">
<head>
<meta charset="utf-8">
<title>QUADRIX – Level Screen</title>
<link href="https://fonts.googleapis.com/css2?family=Montserrat:wght@300;500;700;800&display=swap" rel="stylesheet">
<style>
  :root {
    --stage: #262626;
    --screen-top: #5285d6;
    --screen-bottom: #3b64b2;
    --status-bar: #23427e;
    --header-bar: #2e529a;
    --tile: #233d6e;
    --tile-soft: #2b4b84;
    --tile-active: #6e9de8;
    --accent-box: #4f8ae0;
    --star: #f6c21a;
    --star-off: #3a63b0;
    --ink: #ffffff;
    --ink-soft: #c9dbf6;
  }
  * { box-sizing: border-box; margin: 0; padding: 0; }
  html, body {
    width: 1200px; height: 865px; overflow: hidden;
    background: var(--stage);
    font-family: "Montserrat", sans-serif;
  }
  .screen {
    position: absolute; left: 363px; top: 12px;
    width: 474px; height: 842px; overflow: hidden;
    background: linear-gradient(180deg, var(--screen-top), var(--screen-bottom));
    color: var(--ink);
  }
  .status-bar {
    height: 22px; background: var(--status-bar);
    display: flex; align-items: center; justify-content: space-between;
    padding: 0 8px; font-size: 11px; font-weight: 700;
  }
  .status-bar .carrier, .status-bar .battery { display: flex; align-items: center; gap: 5px; }
  .header-bar {
    height: 50px; background: var(--header-bar);
    display: flex; align-items: center; padding: 0 10px; gap: 14px;
  }
  .pause-button {
    width: 54px; height: 32px; background: var(--accent-box);
    display: flex; align-items: center; justify-content: center;
  }
  .level { display: flex; align-items: center; gap: 8px; font-size: 12px; font-weight: 500; color: var(--ink-soft); margin-left: 40px; }
  .stars { display: flex; gap: 2px; }
  .coins {
    margin-left: auto; width: 70px; height: 32px; background: var(--accent-box);
    display: flex; align-items: center; justify-content: center;
    font-size: 14px; font-weight: 500; color: var(--ink-soft);
  }
  .score {
    position: absolute; left: 88px; top: 112px;
    font-size: 54px; font-weight: 300; letter-spacing: 2px;
  }
  .tile {
    position: absolute; width: 140px; height: 140px; background: var(--tile);
    display: flex; align-items: center; justify-content: center;
    font-size: 64px; font-weight: 800;
  }
  .tile.is-active { background: var(--tile-active); }
  .tile.operator { font-size: 56px; font-weight: 700; }
  .tool {
    position: absolute; width: 60px; height: 60px; background: var(--tile-soft);
    display: flex; align-items: center; justify-content: center;
  }
  .tool.is-faded { opacity: .55; }
</style>
</head>
<body>
<main class="screen">
  <div class="status-bar">
    <span class="carrier">
      <svg width="18" height="10" viewBox="0 0 18 10" aria-hidden="true"><g fill="#fff"><rect x="0" y="7" width="2" height="3"/><rect x="4" y="5" width="2" height="5"/><rect x="8" y="3" width="2" height="7"/><rect x="12" y="1" width="2" height="9"/><rect x="16" y="0" width="2" height="10"/></g></svg>
      NOVA
    </span>
    <span class="clock">10:35 AM</span>
    <span class="battery">
      <svg width="10" height="10" viewBox="0 0 10 10" aria-hidden="true"><circle cx="5" cy="5" r="4.5" fill="#fff"/><path d="M5 2v3h2" stroke="#23427e" fill="none" stroke-width="1.2"/></svg>
      65%
      <svg width="24" height="11" viewBox="0 0 24 11" aria-hidden="true"><rect x=".5" y=".5" width="20" height="10" rx="2" fill="none" stroke="#fff"/><rect x="2" y="2" width="12" height="7" fill="#fff"/><rect x="21" y="3.5" width="2" height="4" fill="#fff"/></svg>
    </span>
  </div>

  <header class="header-bar">
    <div class="pause-button" aria-label="Pause">
      <svg width="16" height="16" viewBox="0 0 16 16" aria-hidden="true"><rect x="2" y="1" width="4" height="14" fill="#c9dbf6"/><rect x="10" y="1" width="4" height="14" fill="#c9dbf6"/></svg>
    </div>
    <div class="level">Level 1
      <span class="stars" aria-label="2 of 3 stars">
        <svg width="60" height="18" viewBox="0 0 60 18" aria-hidden="true">
          <path id="star" d="M9 0l2.6 5.6 6.1.7-4.5 4.2 1.2 6L9 13.5 3.6 16.5l1.2-6L.3 6.3l6.1-.7z" fill="var(--star)"/>
          <path d="M29 0l2.6 5.6 6.1.7-4.5 4.2 1.2 6L29 13.5l-5.4 3 1.2-6-4.5-4.2 6.1-.7z" fill="var(--star)"/>
          <path d="M49 0l2.6 5.6 6.1.7-4.5 4.2 1.2 6L49 13.5l-5.4 3 1.2-6-4.5-4.2 6.1-.7z" fill="var(--star-off)"/>
        </svg>
      </span>
    </div>
    <div class="coins">200</div>
  </header>

  <div class="score">1000</div>

  <div class="tile is-active" style="left:84px;top:220px">1</div>
  <div class="tile" style="left:84px;top:372px">2</div>
  <div class="tile" style="left:84px;top:524px">3</div>
  <div class="tile" style="left:84px;top:676px">4</div>
  <div class="tile operator" style="left:236px;top:220px">+</div>
  <div class="tile operator" style="left:236px;top:372px">−</div>
  <div class="tile operator" style="left:236px;top:524px">×</div>
  <div class="tile operator" style="left:236px;top:676px">÷</div>

  <div class="tool" style="left:392px;top:200px" aria-label="Clear">
    <svg width="26" height="26" viewBox="0 0 26 26" aria-hidden="true"><path d="M4 4l18 18M22 4L4 22" stroke="#1c3360" stroke-width="6"/></svg>
  </div>
  <div class="tool" style="left:392px;top:280px" aria-label="Calculator">
    <svg width="30" height="26" viewBox="0 0 30 26" aria-hidden="true"><rect x="1" y="1" width="28" height="24" fill="none" stroke="#1c3360" stroke-width="2"/><g fill="#1c3360"><rect x="5" y="5" width="20" height="4"/><rect x="5" y="12" width="4" height="3"/><rect x="11" y="12" width="4" height="3"/><rect x="17" y="12" width="4" height="3"/><rect x="5" y="18" width="4" height="3"/><rect x="11" y="18" width="4" height="3"/><rect x="17" y="18" width="4" height="3"/></g></svg>
  </div>
  <div class="tool" style="left:392px;top:360px" aria-label="Hint">
    <svg width="20" height="26" viewBox="0 0 20 26" aria-hidden="true"><path d="M4 8a6 6 0 1 1 8 5.6V17" fill="none" stroke="#1c3360" stroke-width="4"/><rect x="9" y="20" width="5" height="5" fill="#1c3360"/></svg>
  </div>

  <div class="tool" style="left:14px;top:470px" aria-label="Restart">
    <svg width="30" height="30" viewBox="0 0 30 30" aria-hidden="true"><path d="M22 8a10 10 0 1 0 3 8" fill="none" stroke="#1c3360" stroke-width="3"/><path d="M18 3l7 3-3 7z" fill="#1c3360"/></svg>
  </div>
  <div class="tool" style="left:14px;top:550px" aria-label="Redo">
    <svg width="30" height="30" viewBox="0 0 30 30" aria-hidden="true"><path d="M5 26c0-10 6-15 15-15" fill="none" stroke="#1c3360" stroke-width="4"/><path d="M18 4l9 7-9 7z" fill="#1c3360"/></svg>
  </div>
  <div class="tool is-faded" style="left:14px;top:630px" aria-label="Undo">
    <svg width="30" height="30" viewBox="0 0 30 30" aria-hidden="true"><path d="M8 12a9 9 0 1 1 0 8" fill="none" stroke="#1c3360" stroke-width="3"/></svg>
  </div>
  <div class="tool is-faded" style="left:14px;top:710px" aria-label="Confirm">
    <svg width="30" height="30" viewBox="0 0 30 30" aria-hidden="true"><path d="M5 15l7 7 13-14" fill="none" stroke="#1c3360" stroke-width="4"/></svg>
  </div>
</main>
</body>
</html>
```